Business Card Design Project

We recently redesigned our corporate logo and are looking for a business card refreshment.

The business card template should have a place for the following:
Name, Title, email, phone number, instant messenger handle, and the vitals of the company such as the address, main line, web site etc.

PLEASE DO NOT USE OUR EXISTING WEB SITE FOR INSPIRATION as we are redesigning it.

We've attached a picture of our existing business card as an example, although please keep in mind that we have changed the logo (also attached) and encourage your creativity.

Target Market(s)

Information scientists, search professionals, technical people, Ph.Ds, and executives

Industry/Entity Type

Business

Requirements
Must have
• We'll need the template in a format like Illustrator.

```html
<!DOCTYPE html>
<html lang="en">
<head>
<meta charset="utf-8">
<title>HelixTrail Business Card</title>
<link rel="stylesheet" href="https://fonts.googleapis.com/css2?family=Open+Sans:ital,wght@0,400;0,700;1,700&display=swap">
<style>
  :root {
    --bg: #e4e6e6;
    --card-back: #6e7c7a;
    --card-back-light: #8a9694;
    --card-front: #f3f3f2;
    --brand-blue: #1a8fc9;
    --brand-blue-dark: #0f6d9c;
    --text-grey: #555b5c;
    --rule: #b9bdbd;
    --edge: #4d5a59;
  }
  * { margin: 0; padding: 0; box-sizing: border-box; }
  html, body { width: 1200px; height: 900px; overflow: hidden; }
  body {
    background: var(--bg);
    font-family: "Open Sans", Arial, sans-serif;
    position: relative;
  }
  .card {
    position: absolute;
    left: 320px;
    width: 560px;
    height: 320px;
    box-shadow: 0 10px 24px rgba(0,0,0,0.18);
  }
  .card-back {
    top: 60px;
    background: linear-gradient(135deg, var(--card-back) 0%, var(--card-back-light) 100%);
    display: flex;
    align-items: center;
    justify-content: center;
  }
  .brand {
    display: flex;
    align-items: center;
    gap: 10px;
    font-weight: 700;
    color: var(--brand-blue);
    letter-spacing: -0.5px;
  }
  .brand-dot {
    width: 30px; height: 30px;
    border-radius: 50%;
    background: var(--brand-blue);
  }
  .card-back .brand { font-size: 36px; }
  .card-front {
    top: 480px;
    background: var(--card-front);
    border-bottom: 10px solid var(--edge);
  }
  .card-front .brand {
    position: absolute;
    left: 36px; top: 62px;
    font-size: 38px;
  }
  .card-front .brand-dot { width: 34px; height: 34px; }
  .person {
    position: absolute;
    right: 36px; top: 66px;
    text-align: right;
  }
  .person-name { color: var(--brand-blue); font-weight: 700; font-size: 16px; }
  .person-title { color: var(--text-grey); font-size: 13px; }
  .divider {
    position: absolute;
    left: 36px; right: 36px; top: 136px;
    border-top: 1px solid var(--rule);
  }
  .details {
    position: absolute;
    left: 36px; top: 152px;
    color: var(--text-grey);
    font-size: 14px;
    line-height: 21px;
  }
  .contacts {
    display: flex;
    gap: 34px;
    margin-top: 12px;
  }
  .contact-list { list-style: none; }
  .contact-list li { display: flex; align-items: center; gap: 8px; }
  .icon { width: 14px; height: 14px; fill: none; stroke: var(--brand-blue); stroke-width: 1.8; }
  .icon-solid { fill: var(--brand-blue); stroke: none; }
  .accent-band {
    position: absolute;
    left: 0; right: 0; bottom: 6px;
    height: 5px;
    background: var(--brand-blue);
    border-top: 1px solid var(--brand-blue-dark);
  }
</style>
</head>
<body>
  <section class="card card-back">
    <div class="brand"><span class="brand-dot"></span>HelixTrail</div>
  </section>

  <section class="card card-front">
    <div class="brand"><span class="brand-dot"></span>HelixTrail</div>
    <div class="person">
      <div class="person-name">Martin Alvers</div>
      <div class="person-title">Director</div>
    </div>
    <div class="divider"></div>
    <div class="details">
      <address style="font-style:normal">
        Kade van Rozenburg 22-B4 1234 AB, Leeuwarden<br>
        Postbus 4170, 1234 AB, Leeuwarden
      </address>
      <div class="contacts">
        <ul class="contact-list">
          <li>
            <svg class="icon" viewBox="0 0 16 16"><path class="icon-solid" d="M3 1.5l3 3-1.5 2a9 9 0 0 0 5 5l2-1.5 3 3-2 2C6 14.5 1.5 10 1 3z"/></svg>
            415-555-0142
          </li>
          <li>
            <svg class="icon" viewBox="0 0 16 16"><rect class="icon-solid" x="1" y="6" width="14" height="7" rx="1"/><rect x="4" y="2" width="8" height="4"/><rect x="4" y="10" width="8" height="4"/></svg>
            415-555-0143
          </li>
        </ul>
        <ul class="contact-list">
          <li>
            <svg class="icon" viewBox="0 0 16 16"><circle cx="8" cy="8" r="3"/><path d="M11 5v4a2 2 0 0 0 4 0V8a7 7 0 1 0-3 5.7"/></svg>
            martin@helixtrail.com
          </li>
          <li>
            <svg class="icon" viewBox="0 0 16 16"><circle cx="8" cy="8" r="6.5"/><path d="M1.5 8h13M8 1.5c-3 3.5-3 9.5 0 13M8 1.5c3 3.5 3 9.5 0 13"/></svg>
            www.helixtrail.com
          </li>
        </ul>
      </div>
    </div>
    <div class="accent-band"></div>
  </section>
</body>
</html>
```